Australian Sports Podiatry Business needs a Vantor Games marketing flyer

The Stride Clinic is looking for a double sided DLflyer to send out to homes which is targeted at people interested in being fit and healthy. To include:

the Vantor Games logo and colours
sporty background

Are you Set For Vantor?
Whatever Your Goals, We'll Keep You On Track
National and International Sports Experience
Oberin Para Games (and logo if possible)
Tolvane Federation Games (and logo if poss)
Quillan Multisport Global Series (+logo)
Quillan Dravitz Shield Tennis (+logo)

The Stride Clinic name, logo, phone number 9271 6408, website www.harbelstride.net, email info@harbelstride.net

Dr Kamal Ratnavegar's Background:
Kamal's has 20 years experience in the field of Sports Medicine and lower limb biomechanics, and he has had extensive experience with treatment of elite athletes from the Southland Athletic Foundation, the College of Games, the Southland Gannets, Corvale Marauders and the Corvale Pelicans. He was also selected for the HVTB Medical Team to provide Podiatry Services at the Oberin 2000 Para Games, the 2000 GMX Global Multisport Series, the Tolvane 2006 Federation Games and the Quillan 2013 Dravitz Shield. Kamal now treats many athletes from all disciplines in Perth and surrounding areas.

In 1999 Kamal became the Director and Senior Podiatrist for The Stride Clinic in Perth, Western Australia. Since then he has also been a Director of Athletic Health Southland (AHS), WA Director for the Pacific Guild of Podiatric Sports Medicine (PGPSM), and an External Advisor to the Brindlemoor University’s Podiatric Medicine Unit. He is currently road testing minimalist running shoes for optimised performance and injury prevention.

Kamal has always been involved with high level sports, having held a 4x400m Australian Record and also played 1st Division Hockey. He is now training for the Veterans Track Global Meet in October, and volunteers at Kestrow Thunder Junior Runners. He also enjoys keeping fit by running after his 3 kids Mirela, Odette, and Felix.

Target Market(s)

People interested in being fit and healthy

Industry/Entity Type

Medical

Requirements
Must have
• To include:
• the Vantor Games logo and colours
• sporty background
• Are you Set For Vantor?
• Whatever Your Goals, We'll Keep You On Track
• National and International Sports Experience
• Oberin Para Games (and logo if possible)
• Tolvane Federation Games (and logo if poss)
• Quillan Multisport Global Series (+logo)
• Quillan Dravitz Shield Tennis (+logo)
• The Stride Clinic name, logo, phone number 9271 6408, website www.harbelstride.net, email info@harbelstride.net
• Dr Kamal Ratnavegar's Background:
• Kamal's has 20 years experience in the field of Sports Medicine and lower limb biomechanics, and he has had extensive experience with treatment of elite athletes from the Southland Athletic Foundation, the College of Games, the Southland Gannets, Corvale Marauders and the Corvale Pelicans. He was also selected for the HVTB Medical Team to provide Podiatry Services at the Oberin 2000 Para Games, the 2000 GMX Global Multisport Series, the Tolvane 2006 Federation Games and the Quillan 2013 Dravitz Shield. Kamal now treats many athletes from all disciplines in Perth and surrounding areas.
• In 1999 Kamal became the Director and Senior Podiatrist for The Stride Clinic in Perth, Western Australia. Since then he has also been a Director of Athletic Health Southland (AHS), WA Director for the Pacific Guild of Podiatric Sports Medicine (PGPSM), and an External Advisor to the Brindlemoor University’s Podiatric Medicine Unit. He is currently road testing minimalist running shoes for optimised performance and injury prevention.
Nice to have
• Kamal has always been involved with high level sports, having held a 4x400m Australian Record and also played 1st Division Hockey. He is now training for the Veterans Track Global Meet in October, and volunteers at Kestrow Thunder Junior Runners. He also enjoys keeping fit by running after his 3 kids Mirela, Odette, and Felix.

```html
<!DOCTYPE html>
<html lang="en">
<head>
<meta charset="utf-8">
<title>The Stride Clinic – Set For Vantor DL Flyer</title>
<link rel="stylesheet" href="https://fonts.googleapis.com/css2?family=Montserrat:wght@600;700;800;900&family=Open+Sans:wght@400;600&display=swap">
<style>
:root{
  --orange:#f07a1e;
  --orange-deep:#e0601a;
  --navy:#1b3f7c;
  --navy-dark:#132d5c;
  --white:#ffffff;
  --stage:#d9d9dc;
  --ink:#1c1c1c;
}
*{box-sizing:border-box;margin:0;padding:0}
html,body{width:1200px;height:900px;overflow:hidden}
body{background:var(--stage);font-family:"Open Sans",Arial,sans-serif;position:relative}
.flyer{position:absolute;top:40px;width:400px;height:820px;background:var(--white);overflow:hidden;box-shadow:0 6px 18px rgba(0,0,0,.18)}
.flyer--front{left:160px}
.flyer--back{left:640px}

/* ---------- front ---------- */
.headline-block{position:absolute;left:28px;top:34px;font-family:"Montserrat",Arial,sans-serif;font-weight:800;line-height:1}
.headline-block .line-one{color:var(--orange);font-size:34px;letter-spacing:1px}
.headline-block .line-two{color:var(--navy);font-size:40px;letter-spacing:1px;margin-top:4px}
.games-mark{position:absolute;left:210px;top:78px;display:flex;align-items:center;gap:8px}
.games-mark .dot{width:22px;height:22px;border-radius:50%;background:var(--orange)}
.games-mark .name{font-family:"Montserrat",Arial,sans-serif;font-weight:700;font-size:20px;color:var(--navy)}
.stripe-navy{position:absolute;left:0;width:100%;height:12px;background:var(--navy)}
.front-stripe{top:150px}
.hero{position:absolute;left:0;top:162px;width:100%;height:458px;background:radial-gradient(circle at 65% 40%,#f6a04d 0%,var(--orange) 45%,var(--orange-deep) 100%)}
.photo-circle{position:absolute;border-radius:50%;border:5px solid var(--white);box-shadow:0 0 0 2px var(--navy)}
.photo-coach{left:200px;top:6px;width:120px;height:120px;background:linear-gradient(135deg,#e9ecf2,#8c98ad)}
.photo-feet{left:18px;top:74px;width:132px;height:132px;background:linear-gradient(135deg,#d8a27d,#8a5a3a)}
.photo-runners{left:24px;top:214px;width:132px;height:132px;background:linear-gradient(160deg,#7d8fb5,#2b3550)}
.clinic-disc{position:absolute;left:148px;top:106px;width:230px;height:230px;border-radius:50%;background:var(--white);border:4px solid var(--navy);display:flex;flex-direction:column;align-items:center;justify-content:center;gap:12px}
.clinic-mark{display:flex;align-items:center;gap:8px}
.clinic-mark .dot{width:16px;height:16px;border-radius:50%;background:var(--navy)}
.clinic-mark .name{font-family:"Montserrat",Arial,sans-serif;font-weight:700;color:var(--navy)}
.clinic-disc .clinic-mark .name{font-size:20px}
.clinic-disc .clinic-mark{flex-direction:column}
.clinic-disc .clinic-mark .dot{width:60px;height:60px}
.tagline{position:absolute;left:0;top:362px;width:100%;text-align:center;font-family:"Montserrat",Arial,sans-serif}
.tagline h2{color:var(--white);font-size:22px;font-weight:900;line-height:1.12}
.tagline p{color:var(--navy-dark);font-size:13px;font-weight:800;margin-top:8px}
.partners{position:absolute;left:0;top:640px;width:100%;display:flex;justify-content:space-around;align-items:center;padding:0 24px}
.badge{width:60px;height:46px;border-radius:6px}
.badge--a{background:#f4b32a}
.badge--b{background:#c94fa0;border-radius:50%;width:50px}
.badge--c{background:#1d5ea8}
.badge--d{background:#5fb545;border-radius:50%;width:50px}
.web-band{position:absolute;left:0;top:712px;width:100%;height:40px;background:var(--navy);color:var(--white);font-family:"Montserrat",Arial,sans-serif;font-weight:700;font-size:17px;display:flex;align-items:center;justify-content:center}

/* ---------- back ---------- */
.back-logo{position:absolute;left:40px;top:26px}
.back-logo .dot{width:40px;height:40px}
.back-logo .name{font-size:18px}
.stripe-orange{position:absolute;left:0;width:100%;background:var(--orange)}
.back-top-orange{top:118px;height:8px}
.bio-panel{position:absolute;left:0;top:126px;width:100%;height:500px;background:var(--navy)}
.portrait{position:absolute;left:260px;top:70px;width:104px;height:104px;border-radius:50%;border:4px solid var(--white);background:linear-gradient(160deg,#dfe3ea,#9aa6bb);z-index:2}
.bio-title{position:absolute;left:0;top:20px;width:230px;background:var(--orange);padding:8px 14px 8px 40px;font-family:"Montserrat",Arial,sans-serif;font-weight:700;font-size:15px;line-height:1.15}
.bio-title .doctor{color:var(--white);display:block}
.bio-title .label{color:var(--ink);display:block}
.bio-text{position:absolute;left:26px;top:96px;width:348px;color:var(--white);font-size:8.4px;line-height:1.42;text-align:justify}
.bio-text p+p{margin-top:9px}
.back-mid-orange{top:626px;height:22px}
.contact{position:absolute;left:0;top:662px;width:100%;text-align:center;font-family:"Montserrat",Arial,sans-serif}
.contact .call{color:var(--navy);font-size:24px;font-weight:800;letter-spacing:1px}
.contact .email{color:var(--navy);font-size:14px;font-weight:600;margin-top:18px}
.contact .web{color:var(--ink);font-size:14px;font-weight:600;margin-top:4px}
</style>
</head>
<body>

<section class="flyer flyer--front">
  <div class="headline-block">
    <div class="line-one">ARE YOU SET</div>
    <div class="line-two">FOR</div>
  </div>
  <div class="games-mark"><span class="dot"></span><span class="name">Vantor Games</span></div>
  <div class="stripe-navy front-stripe"></div>

  <div class="hero">
    <div class="photo-circle photo-coach" role="img" aria-label="Podiatrist assessing a patient at a treadmill"></div>
    <div class="photo-circle photo-feet" role="img" aria-label="Close-up of bare feet on tiptoe"></div>
    <div class="photo-circle photo-runners" role="img" aria-label="Legs of runners racing on a track"></div>
    <div class="clinic-disc">
      <div class="clinic-mark"><span class="dot"></span><span class="name">The Stride Clinic</span></div>
    </div>
    <div class="tagline">
      <h2>Whatever Your Goals,<br>We'll Keep You On Track</h2>
      <p>National and International Sports Experience</p>
    </div>
  </div>

  <div class="partners">
    <span class="badge badge--a" role="img" aria-label="Partner badge"></span>
    <span class="badge badge--b" role="img" aria-label="Partner badge"></span>
    <span class="badge badge--c" role="img" aria-label="Partner badge"></span>
    <span class="badge badge--d" role="img" aria-label="Partner badge"></span>
  </div>
  <div class="web-band">www.harbelstride.net</div>
</section>

<section class="flyer flyer--back">
  <div class="clinic-mark back-logo"><span class="dot"></span><span class="name">The Stride Clinic</span></div>
  <div class="portrait" role="img" aria-label="Portrait photo of Dr Kamal Ratnavegar"></div>
  <div class="stripe-orange back-top-orange"></div>

  <div class="bio-panel">
    <h1 class="bio-title"><span class="doctor">Dr Kamal Ratnavegar's</span><span class="label">Background:</span></h1>
    <div class="bio-text">
      <p>Kamal's has 20 years experience in the field of Sports Medicine and lower limb biomechanics, and he has had extensive experience with treatment of elite athletes from the Southland Athletic Foundation, the College of Games, the Southland Gannets, Corvale Marauders and the Corvale Pelicans. He was also selected for the HVTB Medical Team to provide Podiatry Services at the Oberin 2000 Para Games, the 2000 GMX Global Multisport Series, the Tolvane 2006 Federation Games and the Quillan 2013 Dravitz Shield. Kamal now treats many athletes from all disciplines in Perth and surrounding areas.</p>
      <p>In 1999 Kamal became the Director and Senior Podiatrist for The Stride Clinic in Perth, Western Australia. Since then he has also been a Director of Athletic Health Southland (AHS), WA Director for the Pacific Guild of Podiatric Sports Medicine (PGPSM), and an External Advisor to the Brindlemoor University’s Podiatric Medicine Unit. He is currently road testing minimalist running shoes for optimised performance and injury prevention.</p>
      <p>Kamal has always been involved with high level sports, having held a 4x400m Australian Record and also played 1st Division Hockey. He is now training for the Veterans Track Global Meet in October, and volunteers at Kestrow Thunder Junior Runners. He also enjoys keeping fit by running after his 3 kids Mirela, Odette, and Felix.</p>
    </div>
  </div>
  <div class="stripe-orange back-mid-orange"></div>

  <div class="contact">
    <div class="call">CALL US: 9271 6408</div>
    <div class="email">EMAIL: info@harbelstride.net</div>
    <div class="web">www.harbelstride.net</div>
  </div>
</section>

</body>
</html>
```